Grand Vessel Soirée Ibiza

We need a flyer to advertise our Super Yacht Party in Ibiza!
This will be more of a template from where all artwork will stem - e.g posters, web img and website so don´t get too hung up on size or orientation this can be anything you want.
We are looking for some unique layout ideas and brand identity that we can carry forward into the whole campaign - there is the potential for a lot of work to spin off from this.
Notes on design:
We are NOT looking for a Nautical Theme. NO portholes of lifeboats or anchors for example.
This is a high class party where customers will be watching the world famous ibiza sunset in front of bar lomavista on a 4 story mega yacht, relaxing on VIP beds, chilling in a Hot Tub, partying in the huge on board dance floor with famous DJ´s playing on a brand new KRELT sound system. The alcohol will be served bottle service with the best champagne and vodka, hot girls in bikinis and sushi served from our on board restaurant.
The flyer needs to ooze class and sophistication while also appealing to party hard music loving lubbers from Ibiza - this will be the tricky part to get right!
It needs to be visual and eye catching - we don't have any pre conceived ideas nessacarily so consider this a blank canvas.
I have attached the company logo and colours some images from pictu vault (don't be concerned about the watermark or low res nature we will look past that in the design) use as many or as few as you want - if you find some others or think it needs a different type feel free to use we can worry about rights etc at a later stage - this is conceptual and will spin off to all brand artwork.
Some wording for the flyer - use as much or as little as you think.
HALCYRA
SUPER YACHT PARTY
IBIZA
EVERY TUESDAY, FRIDAY AND SUNDAY
6PM - SUNSET
WWW.HALCYRAEVENTS.EXAMPLE
RESERVATIONS - VIP@HALCYRAEVENTS.EXAMPLE
NOT ALL BOAT PARTIES ARE CREATED EQUAL
SUPER YACHT EXPERIENCE
ICONIC IBIZA SUNSET
4 FLOORS OF MUSIC
DEEP AND TECH HOUSE
KRELT SOUNDSYSTEM
VIP ROOMS AND BEDS AVAILABLE
ON BOARD LOCAL FASHION & MERCH SHOP
BOTTLE SERVICE TO TABLES
CHAMPAGNE SPRAY
€100 VODKA BOTTLE
WILDEST PARTY
HOTTEST GIRLS AND GUYS
ON BOARD HOT TUB
ISLANDS BEST ARIEL PRODUCTION AT SEA
See following website for inspiration:
http://www.tidelounge-sample.example
http://www.palmcrestresort-sample.example
http://www.zorvaclub.example/destinations/beach-clubs/marbella/
http://www.lunaquay.example
Any questions please ask!
See the following ibiza websites for ideas:http://www.tidelounge-sample.examplehttp://www.palmcrestresort-sample.example Added Saturday, January 17, 2015

```html
<!DOCTYPE html>
<html lang="en">
<head>
<meta charset="utf-8">
<title>Halcyra – Grand Vessel Soirée Ibiza</title>
<link href="https://fonts.googleapis.com/css2?family=Cinzel:wght@400;600&family=Oswald:wght@500&display=swap" rel="stylesheet">
<style>
  :root{
    --stage:#0b0f19;
    --blue-light:#1e4fc4;
    --blue-mid:#123596;
    --blue-deep:#08205f;
    --gold:#e6cf98;
    --gold-dark:#b69654;
    --ink-soft:#c9d6ff;
    --sky-top:#3f5a8f;
    --sea:#6c86b4;
    --deck:#1c2a4a;
  }
  *{margin:0;padding:0;box-sizing:border-box}
  html,body{width:1200px;height:671px;overflow:hidden;background:var(--stage)}
  .flyer{
    position:absolute;left:385px;top:22px;width:430px;height:627px;
    background:radial-gradient(ellipse at 50% 60%,var(--blue-light) 0%,var(--blue-mid) 45%,var(--blue-deep) 100%);
    overflow:hidden;color:var(--gold);font-family:"Cinzel",serif;
  }
  .schedule{position:absolute;top:14px;left:0;right:0;text-align:center;font-family:"Oswald",sans-serif;color:var(--ink-soft)}
  .schedule-days{font-size:8.5px;letter-spacing:.5px}
  .schedule-time{font-size:20px;line-height:1.05;letter-spacing:.5px}
  .deck-photo{
    position:absolute;top:58px;left:0;width:100%;height:260px;
    background:linear-gradient(180deg,var(--sky-top) 0%,var(--sea) 38%,#9aaed0 46%,var(--deck) 62%,var(--blue-mid) 100%);
    -webkit-mask-image:linear-gradient(180deg,#000 70%,transparent 100%);
            mask-image:linear-gradient(180deg,#000 70%,transparent 100%);
  }
  .price-badge{
    position:absolute;top:232px;right:26px;width:50px;height:50px;border-radius:50%;
    background:radial-gradient(circle at 35% 30%,#fffdf4,#d8d2c2 60%,#9c968a);
    color:#1b2a55;text-align:center;font-family:"Oswald",sans-serif;
    display:flex;flex-direction:column;justify-content:center;transform:rotate(-12deg)
  }
  .price-badge .amount{font-size:15px;line-height:1}
  .price-badge .item{font-size:5.5px;letter-spacing:.2px}
  .brand{position:absolute;top:282px;left:0;right:0;text-align:center}
  .rule{display:block;margin:0 auto;width:70px;height:1px;background:var(--gold)}
  .brand-name{font-size:42px;font-weight:600;letter-spacing:1px;line-height:1.05;margin-top:6px}
  .brand-tag{font-size:17px;letter-spacing:1px;line-height:1.1}
  .brand-place{font-size:9px;letter-spacing:6px;margin:2px 0 6px}
  .features{
    position:absolute;top:405px;left:20px;right:20px;
    display:grid;grid-template-columns:repeat(5,1fr);row-gap:10px;column-gap:4px;
    text-align:center;font-size:7px;line-height:1.25;color:var(--gold)
  }
  .reservations{
    position:absolute;top:500px;left:80px;padding:3px 8px;border:1px solid var(--gold-dark);
    font-family:"Oswald",sans-serif;font-size:7.5px;color:#fff;letter-spacing:.4px
  }
  .web{position:absolute;top:532px;right:22px;font-family:"Oswald",sans-serif;font-size:6.5px;color:#fff;letter-spacing:.4px}
  .crest-ornament{position:absolute;top:520px;left:190px;width:50px;height:22px;border-radius:50% 50% 4px 4px;background:linear-gradient(180deg,rgba(230,207,152,.35),rgba(230,207,152,.1))}
</style>
</head>
<body>
  <main class="flyer">
    <header class="schedule">
      <p class="schedule-days">EVERY TUESDAY, FRIDAY AND SUNDAY</p>
      <p class="schedule-time">6:P.M. - SUNSET</p>
    </header>

    <div class="deck-photo" role="img" aria-label="Photo of a super yacht deck at dusk with a hot tub and lounge beds facing the sea"></div>

    <div class="price-badge"><span class="amount">€100</span><span class="item">VODKA BOTTLE</span></div>

    <section class="brand">
      <span class="rule"></span>
      <h1 class="brand-name">HALCYRA</h1>
      <p class="brand-tag">GRAND VESSEL SOIRÉE</p>
      <p class="brand-place">IBIZA</p>
      <span class="rule"></span>
    </section>

    <ul class="features" style="list-style:none">
      <li>Super Yacht<br>Experience</li>
      <li>Iconic<br>Ibiza Sunset</li>
      <li>4 Floors<br>Of Music</li>
      <li>Deep And<br>Tech House</li>
      <li>Krelt<br>Soundsystem</li>
      <li>VIP Rooms And<br>Beds Available</li>
      <li>Bottle Services<br>To Tables</li>
      <li>Champagne<br>Spray</li>
      <li>Wildest Party</li>
      <li></li>
      <li>Hottest<br>Girls and Guys</li>
      <li>Islands Best Ariel<br>Production At Sea</li>
      <li>On Board<br>Hot Tub</li>
    </ul>

    <p class="reservations">FOR RESERVATIONS &nbsp;|&nbsp; VIP@HALCYRAEVENTS.EXAMPLE</p>
    <div class="crest-ornament" role="img" aria-label="Decorative gold flourish"></div>
    <p class="web">WWW.HALCYRAEVENTS.EXAMPLE</p>
  </main>
</body>
</html>
```